Re-design of website: www.velmarpromo.ca/en/

Velmar Promo is a promotional agency specializing in on-site marketing. We are re-designing their website.

We have already produced a prototype:
http://borquelab.com/velmarpromo_siteweb/

The architecture in the prototype must be respected. Please dress up the design with green, grey and black circles and other textures found on their current website www.velmarpromo.ca

Inspiration for design that we like, clean, flat design:

- http://www.tundrafolk.co/
- http://quillborough.com/#!/process
- http://wearedelvani.com/

Delivrables: PSD files of each page of the prototype

Here are the images of their print portfolio: http://ftp.velmarpromo.ca/clients/VMP/VELMARPROMO-PORTFOLIO-2012_EN.zip

Industry/Entity Type

Architecture

Requirements
Must have
• Responsive Design

```html
<!DOCTYPE html>
<html lang="fr">
<head>
<meta charset="utf-8">
<title>Velmar Promo</title>
<link rel="stylesheet" href="https://fonts.googleapis.com/css2?family=Arimo:wght@400;700&display=swap">
<style>
:root{
  --green:#a1cd63;
  --nav-text:#3a2a05;
  --black:#050505;
  --white:#ffffff;
  --heading:#666666;
  --footer:#898989;
  --footer-label:#4a4a4a;
  --footer-text:#3f3f3f;
  --circle-text:#d8d8d8;
  --logo-text:#1c1c1c;
}
*{margin:0;padding:0;box-sizing:border-box}
html,body{width:1200px;height:1000px;overflow:hidden;background:var(--white);font-family:"Arimo",Arial,sans-serif}
.page{position:relative;width:1200px;height:1000px}
.lang{position:absolute;left:841px;top:7px;font-size:9px;color:#222}
.icon-box{position:absolute;width:8px;height:7px;border:1px solid #bbb;background:#eee}
.brand{position:absolute;left:462px;top:28px;display:flex;align-items:center;gap:10px}
.brand-name{font-weight:700;font-size:26px;letter-spacing:2px;color:var(--logo-text);text-transform:uppercase}
.brand-dot{width:30px;height:30px;border-radius:50%;background:var(--green)}
.nav{position:absolute;left:249px;top:84px;width:702px;height:29px;background:var(--green);display:flex;justify-content:center;align-items:center;gap:37px;padding-left:22px}
.nav a{font-size:13px;font-weight:700;color:var(--nav-text);text-decoration:none;letter-spacing:.2px}
.hero{position:absolute;left:249px;top:113px;width:702px;height:245px;background:var(--black);color:var(--white)}
.hero-title{position:absolute;left:0;width:600px;text-align:center;font-weight:400;font-size:56px;line-height:66px;top:60px}
.section-title{position:absolute;left:249px;width:642px;top:378px;text-align:center;font-size:27px;font-weight:400;color:var(--heading)}
.work{position:absolute;width:266px;height:152px}
.footer{position:absolute;left:249px;top:777px;width:702px;height:200px;background:var(--footer)}
.footer-col{position:absolute;top:12px;width:160px}
.footer-label{font-size:10px;color:var(--footer-label)}
.footer-circle{margin:12px 0 0 13px;width:100px;height:100px;border-radius:50%;background:var(--black);color:var(--circle-text);display:flex;align-items:center;justify-content:center;text-align:center;font-size:14px;line-height:16px;box-shadow:0 0 2px rgba(0,0,0,.4)}
.footer-text{margin-top:15px;font-size:7.5px;line-height:9.5px;color:var(--footer-text)}
.copyright{position:absolute;left:249px;top:977px;width:702px;height:21px;background:var(--green);color:var(--white);font-size:14px;line-height:21px;padding-left:59px}
</style>
</head>
<body>
<div class="page">
  <span class="icon-box" style="left:249px;top:2px"></span>
  <span class="icon-box" style="left:249px;top:590px"></span>
  <span class="icon-box" style="left:249px;top:616px"></span>

  <div class="lang">English</div>

  <div class="brand">
    <span class="brand-name">Velmar Promo</span>
    <span class="brand-dot"></span>
  </div>

  <nav class="nav">
    <a href="#">ACCUEIL</a>
    <a href="#">SERVICES</a>
    <a href="#">PROMO 360º</a>
    <a href="#">EMPLOIS</a>
    <a href="#">CONTACT</a>
  </nav>

  <section class="hero">
    <h1 class="hero-title">AGENCY<br>100% PROMO</h1>
  </section>

  <h2 class="section-title">Nos réalisations 360</h2>

  <div class="work" role="img" aria-label="Photo d'une foule de partisans dans la rue lors d'un événement promotionnel" style="left:308px;top:426px;background:linear-gradient(160deg,#7a5a3a,#3a3040 55%,#6b6f75)"></div>
  <div class="work" role="img" aria-label="Photo de participants souriants autour d'une table lors d'un événement extérieur" style="left:600px;top:428px;height:150px;background:linear-gradient(160deg,#9a8d80,#3a3232 55%,#c69a4a)"></div>
  <div class="work" role="img" aria-label="Photo d'une équipe d'hôtesses promotionnelles vêtues de noir" style="left:308px;top:601px;background:linear-gradient(160deg,#7a4a2a,#1e1614 55%,#8a6a58)"></div>
  <div class="work" role="img" aria-label="Affiche d'un concours de bière avec verre et bouteille" style="left:600px;top:601px;background:linear-gradient(90deg,#d8b060,#3a3a3e 35%,#9a9aa2)"></div>

  <footer class="footer">
    <div class="footer-col" style="left:59px">
      <div class="footer-label">Contact.</div>
      <div class="footer-circle">Dummy<br>Text 1</div>
      <p class="footer-text">Lorem ipsum dolor sit amet, consectetur adipisicing elit, sed do eiusmod tempor incididunt ut labore.</p>
    </div>
    <div class="footer-col" style="left:271px">
      <div class="footer-label">Recrutement.</div>
      <div class="footer-circle">Dummy<br>Text 2</div>
      <p class="footer-text">Lorem ipsum dolor sit amet, consectetur adipisicing elit, sed do eiusmod tempor incididunt ut labore.</p>
    </div>
    <div class="footer-col" style="left:483px">
      <div class="footer-label">Suivez-nous.</div>
      <div class="footer-circle">Dummy<br>Text 3</div>
      <p class="footer-text">Lorem ipsum dolor sit amet, consectetur adipisicing elit, sed do eiusmod tempor incididunt ut labore.</p>
    </div>
  </footer>

  <div class="copyright">Copyright © 2013 Kestrel Web Pvt. Ltd. All rights reserved.</div>
</div>
</body>
</html>
```